Maralby Information Posters for Student signage

Secondary school looking for some posters to display throughout the school with fresh designs using school colours and fitting with general feel of the school's graphic image. The final designs should be welcoming but clearly outline the required instructions. Sample designs that have been created by the school are attached with the relevant information that is required to appear on the signs. School would like a more dynamic design than the basic signs attached.
We are looking for:
- Large pop-up banner style size for the 2 posters called
"Ready for class" and "Morning Routine".
- Printable poster for the "Maralby Outdoor" sign.

Please incorporate a design feature of "the Maralby 1,2,3" into the posters and also use the Maralby Leaner values of Integrity, Compassion, Curiosity and Drive to help illustrate the content.

An option for design is to incorporate our school's first nations artwork into the design and i have also provided various extracts of design pieces that the school often uses in it's marketing materials.

Target Market(s)

Secondary School Students

Industry/Entity Type

Education

Colors
00AB8E
00BBA5
67D7C9
C6EFE9
E9F9F6
FFF300
FFF600
FEFA6F
FFFEC7
FFFEE8
FFC000
F8CF3A
FAE287
FDF2CF
FEFAEE

Requirements
Must have
• My project must have eyecatching graphics

```html
<!DOCTYPE html>
<html lang="en">
<head>
<meta charset="utf-8">
<title>Ready for Class – Maralby</title>
<link rel="stylesheet" href="https://fonts.googleapis.com/css2?family=Poppins:wght@600;700;800&family=Arimo:wght@400;700&display=swap">
<style>
  :root {
    --green: #214f31;
    --yellow: #fbe625;
    --white: #ffffff;
    --grey-dot: #b9b9b9;
  }
  * { margin: 0; padding: 0; box-sizing: border-box; }
  html, body { width: 1200px; height: 2823px; overflow: hidden; background: var(--white); }
  .poster { position: relative; width: 1200px; height: 2823px; background: var(--white); overflow: hidden; font-family: "Poppins", sans-serif; color: var(--green); }

  .top-artwork, .bottom-artwork { position: absolute; left: 0; width: 1200px; }
  .top-artwork { top: 0; height: 250px; }
  .bottom-artwork { bottom: 0; height: 420px; }

  .headline {
    position: absolute; top: 318px; left: 0; width: 1200px;
    text-align: center; font-weight: 800; font-size: 150px;
    line-height: 168px; letter-spacing: -2px;
  }

  .checklist-frame {
    position: absolute; left: 66px; top: 838px; width: 1068px; height: 1447px;
    border: 8px solid var(--yellow); border-radius: 64px;
  }

  .steps-tab {
    position: absolute; left: 219px; top: 685px; width: 760px; height: 298px;
    background: var(--yellow); border-radius: 58px; padding: 18px 18px 0;
  }
  .steps-tab::before {
    content: ""; position: absolute; left: -40px; right: -40px; top: 100px; bottom: 0;
    background: var(--white); z-index: -1;
  }
  .steps-title {
    background: var(--white); height: 142px; border-radius: 40px 40px 0 0;
    text-align: center; font-weight: 700; font-size: 92px; line-height: 150px; letter-spacing: -1px;
  }
  .steps-numbers { display: flex; justify-content: space-between; padding: 26px 60px 0 50px; }
  .step-number {
    width: 104px; height: 104px; border-radius: 50%; background: var(--green); color: var(--white);
    font-weight: 800; font-size: 66px; line-height: 106px; text-align: center;
  }

  .check-item { position: absolute; left: 164px; width: 900px; height: 314px; display: flex; align-items: center; }
  .check-item.laptop { top: 1024px; }
  .check-item.phone { top: 1463px; }
  .check-item.uniform { top: 1901px; }
  .item-icon {
    flex: none; width: 314px; height: 314px; border-radius: 50%; background: var(--yellow);
    display: flex; align-items: center; justify-content: center;
  }
  .item-label { margin-left: 37px; font-weight: 700; font-size: 100px; line-height: 92px; letter-spacing: -1px; }
  .item-label .note { display: block; font-size: 62px; line-height: 80px; font-weight: 600; letter-spacing: 0; }

  .divider { position: absolute; left: 164px; width: 872px; border-top: 4px dotted var(--grey-dot); }
  .divider.first { top: 1410px; }
  .divider.second { top: 1848px; }

  .values {
    position: absolute; left: 380px; top: 2640px; width: 520px; text-align: right;
    font-family: "Arimo", sans-serif;
  }
  .values-title { color: var(--white); font-weight: 700; font-size: 46px; line-height: 54px; }
  .values-sub { color: var(--yellow); font-size: 36px; line-height: 44px; }

  .school-name {
    position: absolute; left: 900px; top: 2590px; width: 270px;
    display: flex; flex-direction: column; align-items: center; gap: 14px;
  }
  .school-dot { width: 60px; height: 60px; border-radius: 50%; background: var(--yellow); }
  .school-word { font-family: "Poppins", sans-serif; font-weight: 700; font-size: 48px; color: var(--yellow); }
</style>
</head>
<body>
<main class="poster">
  <svg class="top-artwork" role="img" aria-label="First Nations dotted wave artwork in yellow" viewBox="0 0 1200 250" preserveAspectRatio="none">
    <path d="M0 0 H1200 V40 C1050 110 900 230 700 200 C500 170 250 80 0 210 Z" fill="var(--yellow)"/>
  </svg>

  <h1 class="headline">Are you ready<br>for class?</h1>

  <section class="checklist-frame" aria-label="Checklist"></section>

  <div class="steps-tab">
    <div class="steps-title">The Maralby</div>
    <div class="steps-numbers">
      <span class="step-number">1</span>
      <span class="step-number">2</span>
      <span class="step-number">3</span>
    </div>
  </div>

  <div class="check-item laptop">
    <div class="item-icon">
      <svg width="230" height="170" viewBox="0 0 230 170" aria-hidden="true">
        <rect x="18" y="0" width="194" height="132" rx="12" fill="var(--green)"/>
        <path d="M0 146 H230 V152 C230 162 222 168 212 168 H18 C8 168 0 162 0 152 Z" fill="var(--green)"/>
        <rect x="85" y="146" width="60" height="12" rx="3" fill="none" stroke="var(--yellow)" stroke-width="3"/>
      </svg>
    </div>
    <div class="item-label">Laptop /<br>workbook</div>
  </div>

  <div class="divider first"></div>

  <div class="check-item phone">
    <div class="item-icon">
      <svg width="150" height="230" viewBox="0 0 150 230" aria-hidden="true">
        <path d="M10 60 C10 20 40 4 75 4 C110 4 140 20 140 60 V215 C140 222 134 226 128 226 H22 C16 226 10 222 10 215 Z" fill="none" stroke="var(--green)" stroke-width="6"/>
        <path d="M22 64 C22 30 46 16 75 16 C104 16 128 30 128 64 V212 H22 Z" fill="none" stroke="var(--green)" stroke-width="4"/>
        <circle cx="75" cy="42" r="11" fill="none" stroke="var(--green)" stroke-width="5"/>
        <rect x="30" y="70" width="90" height="134" fill="var(--green)"/>
        <rect x="140" y="90" width="12" height="40" rx="3" fill="none" stroke="var(--green)" stroke-width="4"/>
      </svg>
    </div>
    <div class="item-label">Phone in<br>Lockpouch</div>
  </div>

  <div class="divider second"></div>

  <div class="check-item uniform">
    <div class="item-icon">
      <svg width="230" height="120" viewBox="0 0 230 120" aria-hidden="true">
        <path d="M55 10 C55 2 175 2 175 10 L185 70 H45 Z" fill="var(--green)"/>
        <rect x="48" y="52" width="134" height="14" fill="var(--yellow)"/>
        <path d="M45 70 H185 C215 74 230 88 225 100 C200 116 30 116 5 100 C0 88 15 74 45 70 Z" fill="var(--green)"/>
        <circle cx="75" cy="30" r="4" fill="var(--yellow)"/>
        <circle cx="155" cy="30" r="4" fill="var(--yellow)"/>
      </svg>
    </div>
    <div class="item-label">Correct<br>uniform<span class="note">(Including hat)</span></div>
  </div>

  <svg class="bottom-artwork" role="img" aria-label="First Nations dotted wave artwork in dark green" viewBox="0 0 1200 420" preserveAspectRatio="none">
    <path d="M0 170 C200 110 380 150 520 200 C700 240 820 90 960 40 C1060 10 1140 20 1200 0 V420 H0 Z" fill="var(--green)"/>
  </svg>

  <div class="values">
    <div class="values-title">Curiosity and Drive</div>
    <div class="values-sub">Maralby Learner Values</div>
  </div>

  <div class="school-name">
    <span class="school-dot"></span>
    <span class="school-word">Maralby</span>
  </div>
</main>
</body>
</html>
```